homepage design , industry automation control image

we need a design , based on our Logo image.

we focus on selling of temprature sensor ,and parts.

but need concept or image on industry automation control

we need enviroment friendly concept.

Industry/Entity Type

Industry

Number of Pages Required

5+ page

Requirements
Must have
• we need a Cartoon Image of a Temperature sensor,
• attaching a Excel file with the sensor looking.
Nice to have
• Nature image, future concept

```html
<!DOCTYPE html>
<html lang="en">
<head>
<meta charset="utf-8">
<title>Veldhaus Messtechnik</title>
<link href="https://fonts.googleapis.com/css2?family=Roboto:wght@300;400;500;700&display=swap" rel="stylesheet">
<style>
:root{
  --green:#6cc400;
  --green-dark:#0f8a00;
  --lime:#aaff00;
  --leaf:#5aa800;
  --footer:#0a8a00;
  --footer-side:#007800;
  --text:#333;
  --muted:#666;
  --band:#f7f7f7;
  --medical:#5e0f10;
  --military:#3d7340;
  --automotive:#235f6f;
  --industrial:#d88a05;
}
*{margin:0;padding:0;box-sizing:border-box}
html,body{width:1200px;height:2597px;overflow:hidden;background:#fff}
body{position:relative;font-family:'Roboto',sans-serif;color:var(--text)}
.abs{position:absolute}

/* header */
.site-header{position:absolute;left:0;top:0;width:1200px;height:64px;background:#fff}
.brand{position:absolute;left:90px;top:14px;display:flex;align-items:center;gap:10px;font-size:22px;font-weight:500;color:var(--green)}
.brand-square{width:34px;height:34px;background:var(--green)}
.nav{position:absolute;left:478px;top:0;height:64px;display:flex;align-items:center;font-size:12px;text-transform:uppercase;color:#333}
.nav a{position:absolute;white-space:nowrap;color:inherit;text-decoration:none}
.nav .active{color:var(--green-dark);border-top:2px solid var(--green-dark);padding-top:22px;top:0}
.nav-caret{font-size:9px;margin-left:4px}
.call-btn{position:absolute;left:958px;top:14px;width:152px;height:38px;border-radius:19px;background:var(--green);color:#fff;font-size:12px;font-weight:500;display:flex;align-items:center;justify-content:center;gap:7px}

/* hero */
.hero{position:absolute;left:0;top:64px;width:1200px;height:563px;background:linear-gradient(90deg,var(--lime) 0%,#99ee00 45%,var(--leaf) 100%)}
.hero-blob{position:absolute;left:405px;top:58px}
.hero-sensor{position:absolute;left:520px;top:100px;width:140px;height:430px;border-radius:30px;background:linear-gradient(180deg,#e8e8e8,#bdbdbd)}
.hero-title{position:absolute;right:689px;top:220px;text-align:right;color:var(--green-dark);font-weight:700;line-height:1}
.hero-title .l1{font-size:50px}
.hero-title .l2{font-size:56px;margin-top:4px}
.slide-arrow{position:absolute;top:248px;width:31px;height:69px;background:rgba(0,0,0,.35);display:flex;align-items:center;justify-content:center}
.scroll-down{position:absolute;left:592px;top:606px;width:42px;height:42px;border-radius:50%;background:#fff;box-shadow:0 2px 6px rgba(0,0,0,.2);display:flex;align-items:center;justify-content:center;z-index:2}

/* about */
.about-photo{position:absolute;left:88px;top:724px;width:418px;height:303px;background:linear-gradient(180deg,#c6dbee 0%,#a9c6df 55%,#5f7e6d 72%,#3f6f8f 100%);clip-path:polygon(0 0,100% 0,77% 100%,0 100%)}
.about-rule{position:absolute;left:476px;top:780px;width:61px;height:2px;background:var(--green)}
.about-text{position:absolute;left:566px;top:748px;width:525px}
.eyebrow{font-size:11px;color:#999}
.about-title{font-size:29px;font-weight:400;color:#222;margin-top:6px;display:flex;align-items:center;gap:20px}
.about-title span{color:var(--green)}
.about-title i{flex:1;height:22px;background:#f3f3f3}
.about-text p{font-size:12.5px;line-height:20px;color:var(--muted);margin-top:14px}
.about-text .label{color:var(--green)}
.btn-more{display:inline-block;margin-top:22px;padding:0 21px;height:33px;line-height:33px;border-radius:17px;background:var(--green);color:#fff;font-size:10px;font-weight:700}

/* industries */
.industries{position:absolute;left:0;top:1115px;width:1200px;height:508px;background:var(--band)}
.ind-title{position:absolute;left:88px;top:130px;font-size:29px;font-weight:400;line-height:33px;color:#222}
.ind-lead{position:absolute;left:88px;top:202px;width:500px;font-size:12px;line-height:18px;color:#444}
.tile{position:absolute;top:260px;width:134px;height:140px;color:#fff;font-size:13px;display:flex;flex-direction:column;align-items:center;justify-content:flex-end;padding-bottom:22px;gap:18px;border:2px solid rgba(0,0,0,.08)}
.ind-visual{position:absolute;left:814px;top:124px;width:386px;height:252px;border-radius:10px 0 0 10px;background:linear-gradient(110deg,#f0f0f0,#d2d2d2 60%,#ececec)}

/* blog */
.blog-title{position:absolute;left:0;top:1692px;width:1200px;text-align:center;font-size:30px;font-weight:400;color:#222}
.blog-photo{position:absolute;top:1756px;width:497px;height:220px}
.post{position:absolute;top:2016px;width:497px}
.date{position:absolute;left:0;top:0;width:55px;height:66px;background:var(--green);color:#fff;text-align:center}
.date b{display:block;font-size:29px;font-weight:400;line-height:40px;padding-top:4px}
.date small{font-size:8px;text-transform:uppercase}
.post h3{margin-left:71px;font-size:15px;font-weight:400;color:#222;padding-top:4px}
.post p{margin-left:71px;font-size:11.5px;line-height:19px;color:#666;margin-top:6px}

/* partners */
.partner{position:absolute;top:2163px;width:196px;height:77px;border:1px solid #e6e6e6;display:flex;align-items:center;justify-content:center}
.partner-shape{width:110px;height:26px;background:#d4d4d4;border-radius:3px}

/* footer */
.footer{position:absolute;left:0;top:2300px;width:1200px;height:297px;background:var(--footer);color:#fff}
.footer-side{position:absolute;left:0;top:0;width:343px;height:297px;background:var(--footer-side);display:flex;align-items:center;justify-content:center;gap:10px;font-size:20px;font-weight:500}
.footer-side .sq{width:28px;height:28px;border:3px solid #fff}
.f-col{position:absolute;top:74px;font-size:12px}
.f-col h4{font-size:13px;font-weight:700;text-transform:uppercase;margin-bottom:16px}
.f-col li{list-style:none;height:22.5px}
.contact-row{display:flex;gap:12px;line-height:19px;margin-bottom:6px}
.contact-row svg{flex:none;margin-top:3px}
.f-input{width:216px;height:40px;background:#0f7a0a;font-size:11px;color:#cfe;padding:13px 16px}
.f-btn{margin-top:9px;width:119px;height:40px;background:var(--lime);color:#0b6a00;font-size:11px;font-weight:700;display:flex;align-items:center;justify-content:center;text-transform:uppercase;color:#fff;background:#7fd500}
.f-rule{position:absolute;left:400px;top:250px;width:710px;height:1px;background:rgba(255,255,255,.15)}
.f-copy{position:absolute;left:400px;top:268px;font-size:11px}
.f-legal{position:absolute;right:90px;top:268px;font-size:11px}
.to-top{position:absolute;left:1132px;top:233px;width:30px;height:30px;border-radius:50%;background:#fff;display:flex;align-items:center;justify-content:center}
</style>
</head>
<body>

<header class="site-header">
  <div class="brand"><span class="brand-square"></span>Veldhaus Messtechnik</div>
  <nav class="nav">
    <a class="active" style="left:0">Home</a>
    <a style="left:66px">Industries<span class="nav-caret">&#8964;</span></a>
    <a style="left:168px">Services<span class="nav-caret">&#8964;</span></a>
    <a style="left:256px">Company<span class="nav-caret">&#8964;</span></a>
    <a style="left:346px">Contact</a>
    <a style="left:427px;top:25px">
      <svg width="16" height="16" viewBox="0 0 16 16" fill="none" stroke="#888" stroke-width="1.6"><circle cx="7" cy="7" r="5"/><path d="M11 11l4 4"/></svg>
    </a>
  </nav>
  <div class="call-btn">
    <svg width="12" height="12" viewBox="0 0 24 24" fill="#fff"><path d="M6.6 10.8a15 15 0 006.6 6.6l2.2-2.2a1 1 0 011-.25 11.4 11.4 0 003.6.6 1 1 0 011 1V20a1 1 0 01-1 1A17 17 0 013 4a1 1 0 011-1h3.5a1 1 0 011 1c0 1.25.2 2.45.6 3.6a1 1 0 01-.25 1z"/></svg>
    (000) 555-0142
  </div>
</header>

<section class="hero">
  <svg class="hero-blob" width="400" height="420" viewBox="0 0 400 420">
    <path d="M175 20C225-10 265 20 300 95C345 190 400 280 360 345C325 405 240 405 150 385C60 365 5 335 15 270C25 200 110 60 175 20Z" fill="#fff"/>
  </svg>
  <div class="hero-sensor" role="img" aria-label="Cartoon temperature sensor with connection head and long probe"></div>
  <div class="hero-title"><div class="l1">VELDHAUS</div><div class="l2">Messtechnik</div></div>
  <div class="slide-arrow" style="left:0"><svg width="8" height="12" viewBox="0 0 8 12"><path d="M6 1L1 6l5 5" fill="none" stroke="#fff" stroke-width="1.6"/></svg></div>
  <div class="slide-arrow" style="left:1169px"><svg width="8" height="12" viewBox="0 0 8 12"><path d="M2 1l5 5-5 5" fill="none" stroke="#fff" stroke-width="1.6"/></svg></div>
</section>
<div class="scroll-down"><svg width="10" height="7" viewBox="0 0 10 7"><path d="M1 1l4 4 4-4" fill="none" stroke="#333" stroke-width="1.6"/></svg></div>

<section class="about">
  <div class="about-photo" role="img" aria-label="Tall office tower beside a river under a pale blue sky"></div>
  <div class="about-rule"></div>
  <div class="about-text">
    <div class="eyebrow">Know more about us</div>
    <h2 class="about-title">About <span>VM</span><i></i></h2>
    <p>Lorem ipsum dolor sit amet, consectetuer adipiscing elit. Aenean commodo ligula eget dolor. Aenean massa. Cum sociis natoque penatibus et magnis dis parturient montes, nascetur ridiculus mus. Donec quam felis, ultricies nec, pellentesque eu, pretium quis, sem. Nulla consequat massa quis enim donec pede justo .</p>
    <p><span class="label">Mission :</span> Lorem ipsum dolor sit amet, consectetuer adipiscing elit. Aenean commodo ligula eget dolor. Aenean massa. Cum sociis natoque penatibus.</p>
    <span class="btn-more">READ MORE</span>
  </div>
</section>

<section class="industries">
  <h2 class="ind-title">Building connections for a variety<br>of industries</h2>
  <p class="ind-lead">Lorem ipsum dolor sit amet, consectetuer adipiscing elit. Aenean commodo ligula eget dolor. Aenean massa. Cum sociis natoque penatibus et .</p>
  <div class="tile" style="left:90px;background:var(--medical)">
    <svg width="52" height="42" viewBox="0 0 52 42"><rect x="2" y="8" width="48" height="32" rx="4" fill="#fff"/><rect x="18" y="2" width="16" height="8" rx="2" fill="none" stroke="#fff" stroke-width="3"/><circle cx="26" cy="24" r="11" fill="var(--medical)"/><path d="M23 17h6v4h4v6h-4v4h-6v-4h-4v-6h4z" fill="#fff"/></svg>
    Medical
  </div>
  <div class="tile" style="left:258px;background:var(--military)">
    <svg width="46" height="44" viewBox="0 0 46 44"><path d="M23 2c2 0 3 3 3 6v10l18 10v4l-18-5v9l5 4v3l-8-2-8 2v-3l5-4v-9L2 32v-4l18-10V8c0-3 1-6 3-6z" fill="#fff"/></svg>
    Military
  </div>
  <div class="tile" style="left:424px;background:var(--automotive)">
    <svg width="60" height="36" viewBox="0 0 60 36"><rect x="2" y="4" width="34" height="22" fill="#fff"/><path d="M38 10h12l8 9v7H38z" fill="#fff"/><circle cx="13" cy="29" r="5" fill="#fff" stroke="var(--automotive)" stroke-width="2"/><circle cx="48" cy="29" r="5" fill="#fff" stroke="var(--automotive)" stroke-width="2"/></svg>
    Automotive
  </div>
  <div class="tile" style="left:591px;background:var(--industrial)">
    <svg width="48" height="42" viewBox="0 0 48 42"><path d="M4 40V8h6v14l10-7v7l10-7v7l10-7v25z" fill="#fff"/><rect x="10" y="28" width="5" height="5" fill="var(--industrial)"/><rect x="20" y="28" width="5" height="5" fill="var(--industrial)"/><rect x="30" y="28" width="5" height="5" fill="var(--industrial)"/></svg>
    Industrial
  </div>
  <div class="ind-visual" role="img" aria-label="Two cartoon temperature sensors with connection heads and probes"></div>
</section>

<section class="blog">
  <h2 class="blog-title">Latest Blog</h2>
  <div class="blog-photo" style="left:97px;background:linear-gradient(180deg,#6e5f80 0%,#8a7a8f 45%,#3b3a40 70%,#1f1f24 100%)" role="img" aria-label="City skyline with skyscrapers at dusk"></div>
  <div class="blog-photo" style="left:604px;background:linear-gradient(180deg,#e9c7a0 0%,#d99a62 35%,#6a5a4e 65%,#2f2c2c 100%)" role="img" aria-label="Aerial view of a city at sunset beside a lake"></div>
  <article class="post" style="left:118px">
    <div class="date"><b>29</b><small>July</small></div>
    <h3>Customer Around The World Satisfy With It</h3>
    <p>Consectetur adipisicing elit, sed do eiusmod tempor incididunt ut labore et dolore magna aliqua quis [...]</p>
  </article>
  <article class="post" style="left:627px">
    <div class="date"><b>29</b><small>July</small></div>
    <h3>Customer Around The World Satisfy With It</h3>
    <p>Consectetur adipisicing elit, sed do eiusmod tempor incididunt ut labore et dolore magna aliqua quis [...]</p>
  </article>
</section>

<section class="partners">
  <div class="partner" style="left:90px"><span class="partner-shape"></span></div>
  <div class="partner" style="left:296px"><span class="partner-shape"></span></div>
  <div class="partner" style="left:502px"><span class="partner-shape"></span></div>
  <div class="partner" style="left:708px"><span class="partner-shape"></span></div>
  <div class="partner" style="left:914px"><span class="partner-shape"></span></div>
</section>

<footer class="footer">
  <div class="footer-side"><span class="sq"></span>Veldhaus</div>
  <div class="f-col" style="left:410px">
    <h4>Useful Links</h4>
    <ul>
      <li>&rsaquo;&nbsp; Home</li>
      <li>&rsaquo;&nbsp; Industries</li>
      <li>&rsaquo;&nbsp; Services</li>
      <li>&rsaquo;&nbsp; Company</li>
      <li>&rsaquo;&nbsp; Contact</li>
    </ul>
  </div>
  <div class="f-col" style="left:627px">
    <h4>Contact Info</h4>
    <div class="contact-row"><svg width="10" height="13" viewBox="0 0 10 13"><path d="M5 0a5 5 0 015 5c0 4-5 8-5 8S0 9 0 5a5 5 0 015-5z" fill="#fff"/><circle cx="5" cy="5" r="2" fill="var(--footer)"/></svg><span>48 Linden Row, Fairhollow,<br>UT 84021</span></div>
    <div class="contact-row"><svg width="11" height="11" viewBox="0 0 24 24" fill="#fff"><path d="M6.6 10.8a15 15 0 006.6 6.6l2.2-2.2a1 1 0 011-.25 11.4 11.4 0 003.6.6 1 1 0 011 1V20a1 1 0 01-1 1A17 17 0 013 4a1 1 0 011-1h3.5a1 1 0 011 1c0 1.25.2 2.45.6 3.6a1 1 0 01-.25 1z"/></svg><span>(012) 555-0199</span></div>
    <div class="contact-row"><svg width="12" height="9" viewBox="0 0 12 9"><rect width="12" height="9" fill="#fff"/><path d="M0 0l6 5 6-5" fill="none" stroke="var(--footer)" stroke-width="1.2"/></svg><span>sales@veldhaus-mt.com</span></div>
  </div>
  <div class="f-col" style="left:894px">
    <h4>Newsletter</h4>
    <div class="f-input">Your Email</div>
    <div class="f-btn">Subscribe</div>
  </div>
  <div class="f-rule"></div>
  <div class="f-copy">Copyright 2017 | All Right Reseved</div>
  <div class="f-legal">Terms &amp; Conditions | Privacy Policy</div>
  <div class="to-top"><svg width="10" height="7" viewBox="0 0 10 7"><path d="M1 6l4-4 4 4" fill="none" stroke="#333" stroke-width="1.6"/></svg></div>
</footer>

</body>
</html>
```